Start up in business consultancy needs a business card

We need the business card's layout (we have already the logo). Our business is concerned on consultancy services delivered to companies on the matter of sustainability. Business card should be enough essentials and professional style.

Side A with the following info:
logo + a space for the claim (still to identify) + website of the company

Side B with the following info:
Name of business card holder + title of the business card holder + address of the company + space for mobile number, phone number, fax number + e-mail of business card holder + graphic details around.

Target Market(s)

Business of any sector

Industry/Entity Type

Business Service

Contact Information for Business Card

Name of the company:
Pianoverde srl
Società Benefit

Address of the company:
Via Lucerna, 7
21047 - Saronno (VA)

Website:
www.pianoverde.it

Name of the BC' holder:
Luca Ferentino

Title:
Co-fondatore

Email:
luca@pianoverde.it

Mobile:
+39 348 915 2074
Phone:
+39 348 915 2074
Fax:
+39 348 915 2074

Font styles to use
Other font styles liked:
• new gothic

```html
<!DOCTYPE html>
<html lang="it">
<head>
<meta charset="utf-8">
<title>Pianoverde – biglietto da visita</title>
<link rel="stylesheet" href="https://fonts.googleapis.com/css2?family=Open+Sans:wght@400;600;700&display=swap">
<style>
  :root {
    --backdrop: #e9e7e4;
    --card-blue: #1f6fb4;
    --card-black: #1b1b1b;
    --ink-light: #ffffff;
    --ink-soft: #e6e6e6;
    --rule: #d9d9d9;
    --shadow: rgba(0,0,0,0.22);
  }
  * { box-sizing: border-box; margin: 0; padding: 0; }
  html, body {
    width: 1200px; height: 844px; overflow: hidden;
    background: var(--backdrop);
    font-family: "Open Sans", Arial, sans-serif;
  }
  .stage {
    position: relative; width: 1200px; height: 844px;
    display: flex; align-items: center; justify-content: center; gap: 60px;
  }
  .card {
    position: relative; width: 510px; height: 310px;
    box-shadow: 0 10px 28px var(--shadow);
    color: var(--ink-light);
  }
  /* Front: holder details */
  .card--front { background: var(--card-blue); }
  .brand {
    position: absolute; display: flex; align-items: center; gap: 12px;
    font-weight: 400; color: var(--ink-light); letter-spacing: -0.5px;
  }
  .brand__dot {
    width: 30px; height: 30px; border: 3px solid var(--ink-light); border-radius: 50%;
  }
  .card--front .brand { right: 40px; top: 108px; font-size: 34px; }
  .holder { position: absolute; left: 40px; top: 130px; }
  .holder__name { font-size: 17px; font-weight: 700; line-height: 1.2; }
  .holder__title { font-size: 13px; line-height: 1.4; }
  .address { position: absolute; left: 58px; top: 186px; font-size: 13px; line-height: 1.35; }
  .contacts { position: absolute; left: 58px; top: 230px; list-style: none; }
  .contacts li {
    display: flex; align-items: center; gap: 9px;
    font-size: 13px; line-height: 17px;
  }
  .contacts svg { width: 11px; height: 11px; fill: var(--ink-light); flex: none; }

  /* Back: company side */
  .card--back { background: var(--card-black); text-align: center; }
  .card--back .brand { left: 50%; transform: translateX(-50%); top: 40px; font-size: 32px; }
  .benefits { position: absolute; left: 0; right: 0; top: 108px; }
  .benefits__title { font-size: 13px; font-weight: 700; margin-bottom: 8px; }
  .benefits__list { font-size: 12px; line-height: 1.4; color: var(--ink-soft); }
  .site-row {
    position: absolute; left: 0; right: 0; top: 196px;
    display: flex; align-items: center; gap: 14px; padding: 0 30px;
  }
  .site-row__rule { flex: 1; height: 1px; background: var(--rule); }
  .site-row__url { font-size: 12px; color: var(--ink-soft); }
  .base-rule { position: absolute; left: 30px; right: 30px; bottom: 30px; height: 1px; background: var(--rule); }
</style>
</head>
<body>
<main class="stage">
  <section class="card card--front" aria-label="Fronte biglietto">
    <div class="brand"><span class="brand__dot"></span><span class="brand__name">pianoverde</span></div>
    <div class="holder">
      <p class="holder__name">Luca Ferentino</p>
      <p class="holder__title">Co-fondatore</p>
    </div>
    <p class="address">Via Lucerna, 7<br>21047 - Saronno (VA)</p>
    <ul class="contacts">
      <li><svg viewBox="0 0 12 12"><path d="M3 0h6a1 1 0 0 1 1 1v10a1 1 0 0 1-1 1H3a1 1 0 0 1-1-1V1a1 1 0 0 1 1-1zm0 1.5v8h6v-8z"/></svg>+39 348 915 2074</li>
      <li><svg viewBox="0 0 12 12"><path d="M2.5 0.5 4.5 3 3.5 4.5c.8 1.7 2.2 3.1 4 4L9 7.5l2.5 2-1 2C5 11.5.5 7 .5 1.5z"/></svg>+39 348 915 2074</li>
      <li><svg viewBox="0 0 12 12"><path d="M3 0h5v3H3zM1 4h10v6H9v2H3v-2H1zm3 4v3h4V8z"/></svg>+39 348 915 2074</li>
      <li><svg viewBox="0 0 12 12"><path d="M0 2h12v1L6 7 0 3zm0 2.3 6 4 6-4V10H0z"/></svg>luca@pianoverde.it</li>
    </ul>
  </section>

  <section class="card card--back" aria-label="Retro biglietto">
    <div class="brand"><span class="brand__dot"></span><span class="brand__name">pianoverde</span></div>
    <div class="benefits">
      <p class="benefits__title">Company Benefits</p>
      <p class="benefits__list">Benfit point One | Benfit point Two<br>Benfit point Three | Benfit point Four<br>Benfit point Five</p>
    </div>
    <div class="site-row">
      <span class="site-row__rule"></span>
      <span class="site-row__url">www.pianoverde.it</span>
      <span class="site-row__rule"></span>
    </div>
    <span class="base-rule"></span>
  </section>
</main>
</body>
</html>
```